Personal Trainer and Corporate Health Business

I need a business card for a new company I'm starting in Australia called "Brisk Vitality Partners" I will be providing a Personal training service as well as corporate health in companies.
The service provided is to help promote an active and healthy lifstyle.
The design should communicate a healthy lifestyle and also the benefits that this can have on a personal level and in the corporate environment and the benefits that flow from that.

Target Market(s)

Members of the public and Corporate

Industry/Entity Type

Environment

Requirements
Must have
• Company logo attached
Look and feel fresh and modern

Tag line: "Moving together to better living"

Lewis Norgate
Managing Director

m: 0417 596 304
e: lewis@briskvitalitypartners.com.au

www.briskvitalitypartners.com.au
Nice to have
• Can be 1 or 2 sided

```html
<!DOCTYPE html>
<html lang="en">
<head>
<meta charset="utf-8">
<title>Brisk Vitality Partners – Business Card</title>
<link rel="stylesheet" href="https://fonts.googleapis.com/css2?family=Arimo:wght@400;700&display=swap">
<style>
  :root {
    --backdrop: #e4e0db;
    --card-black: #141414;
    --card-black-light: #262626;
    --lime: #a8d433;
    --brand-blue: #1d68a3;
    --link-blue: #3b86c6;
    --white: #ffffff;
    --muted-white: #e6e6e6;
  }
  * { box-sizing: border-box; margin: 0; padding: 0; }
  html, body {
    width: 1200px;
    height: 803px;
    overflow: hidden;
  }
  body {
    background: var(--backdrop);
    font-family: "Arimo", Arial, sans-serif;
    position: relative;
  }
  .card {
    position: absolute;
    top: 140px;
    width: 330px;
    height: 524px;
    border-radius: 20px;
    overflow: hidden;
    background: radial-gradient(ellipse at 40% 30%, var(--card-black-light), var(--card-black) 75%);
    box-shadow: 0 10px 28px rgba(0, 0, 0, 0.28);
  }
  .card--front { left: 220px; }
  .card--back { left: 650px; }

  /* Front */
  .brand {
    position: absolute;
    top: 78px;
    left: 0;
    right: 0;
    display: flex;
    flex-direction: column;
    align-items: center;
    gap: 14px;
  }
  .brand__dot {
    width: 44px;
    height: 44px;
    border-radius: 50%;
    background: var(--lime);
  }
  .brand__name {
    color: var(--brand-blue);
    font-size: 27px;
    font-weight: 700;
    text-align: center;
    line-height: 1.15;
    letter-spacing: 0.5px;
  }
  .person {
    position: absolute;
    top: 262px;
    left: 34px;
  }
  .person__name {
    font-size: 25px;
    letter-spacing: 1.5px;
    color: var(--white);
  }
  .person__surname { color: var(--lime); }
  .person__role {
    margin-top: 6px;
    margin-left: 70px;
    font-size: 17px;
    letter-spacing: 1px;
    color: var(--link-blue);
  }
  .contact {
    position: absolute;
    top: 350px;
    left: 34px;
    list-style: none;
    color: var(--muted-white);
    font-size: 12.5px;
    line-height: 1.65;
    letter-spacing: 0.6px;
  }
  .accent-stripe {
    position: absolute;
    left: 0;
    right: 0;
    top: 424px;
    height: 12px;
    background: var(--lime);
  }
  .accent-band {
    position: absolute;
    left: 0;
    right: 0;
    top: 436px;
    bottom: 0;
    background: var(--brand-blue);
  }

  /* Back */
  .tagline {
    position: absolute;
    left: 26px;
    bottom: 70px;
    font-family: "Arimo", Arial, sans-serif;
    font-weight: 700;
    font-size: 26px;
    line-height: 1.75;
    letter-spacing: 5px;
    text-transform: uppercase;
    color: var(--lime);
  }
  .tagline__line { display: block; }
  .tagline__quote { color: var(--link-blue); }
</style>
</head>
<body>
  <section class="card card--front" aria-label="Business card front">
    <div class="brand">
      <span class="brand__dot" aria-hidden="true"></span>
      <p class="brand__name">BRISK VITALITY<br>PARTNERS</p>
    </div>
    <div class="person">
      <p class="person__name">Lewis <span class="person__surname">Norgate</span></p>
      <p class="person__role">Managing Director</p>
    </div>
    <ul class="contact">
      <li>0417 596 304</li>
      <li>lewis@briskvitalitypartners.com.au</li>
      <li>www.briskvitalitypartners.com.au</li>
    </ul>
    <div class="accent-stripe"></div>
    <div class="accent-band"></div>
  </section>

  <section class="card card--back" aria-label="Business card back">
    <p class="tagline">
      <span class="tagline__line"><span class="tagline__quote">"</span>Moving</span>
      <span class="tagline__line">Together</span>
      <span class="tagline__line">to Better</span>
      <span class="tagline__line">Living<span class="tagline__quote">"</span></span>
    </p>
  </section>
</body>
</html>
```